Stationery Design Project - Red Anvil Workforce

Red Anvil Workforce Staff
*Perth *Brisbane

Business Cards
Size: 90mm x 55mm
Letterhead
Size: A4 - 210mm x 297mm
With Compliments Slip
Size: DL - 210mm x 99mm
Notepad
Size: 250mm x 140mm
Presentation Folder
Size: A4

Phone: 08 9471 3826
Email: info@redanvilworkforce.example.com.au
website: www.redanvilworkforce.example.com.au
Address: 417 Tamber Road
Marrowdale Northshire 6190

-
Business cards:

Neil Dawson
Managing Director
Phone: 08 9471 3826
Mobile: 0477 863 150
Email: neild@redanvilworkforce.example.com.au
Address: 417 Tamber Road
-
Its a new manpower (Recruitment Agency) that employs blue collar workers eg: fitters, welders, drivers and warehouse people

If you need any further information please contact myself

Cheers

Neil

```html
<!DOCTYPE html>
<html lang="en">
<head>
<meta charset="utf-8">
<title>Red Anvil Workforce – Business Card</title>
<link href="https://fonts.googleapis.com/css2?family=Arimo:wght@400;700&display=swap" rel="stylesheet">
<style>
  :root {
    --stage: #3a3a3c;
    --navy-deep: #0a2747;
    --navy: #14487a;
    --sky: #2f8fd0;
    --sky-light: #7cc8f2;
    --brand-blue: #1b7fc3;
    --paper: #fbfbfb;
    --paper-shade: #ececec;
    --ink-grey: #8c8c8c;
    --rule: #9a9a9a;
    --white: #ffffff;
  }
  * { margin: 0; padding: 0; box-sizing: border-box; }
  html, body { width: 1200px; height: 900px; overflow: hidden; }
  body {
    background: var(--stage);
    font-family: "Arimo", Arial, sans-serif;
    display: flex;
    flex-direction: column;
    align-items: center;
    justify-content: center;
    gap: 60px;
  }
  .card {
    position: relative;
    width: 540px;
    height: 330px;
    border-radius: 16px;
    overflow: hidden;
  }

  /* Front */
  .card--front {
    background: linear-gradient(120deg, var(--navy-deep) 0%, var(--navy) 55%, var(--sky) 100%);
  }
  .front-artwork {
    position: absolute;
    right: -40px;
    top: -30px;
    width: 380px;
    height: 330px;
    border-radius: 50%;
    background: radial-gradient(ellipse at 50% 55%, var(--sky-light) 0%, var(--sky) 40%, rgba(47,143,208,0) 72%);
  }
  .front-brand {
    position: absolute;
    left: 36px;
    top: 128px;
    display: flex;
    align-items: center;
    gap: 14px;
  }
  .brand-dot {
    width: 38px;
    height: 38px;
    border-radius: 50%;
    background: var(--sky);
    flex: none;
  }
  .brand-name {
    font-weight: 700;
    font-size: 15px;
    letter-spacing: 0.22em;
    text-transform: uppercase;
    white-space: nowrap;
  }
  .front-brand .brand-name { color: var(--white); }
  .front-web {
    position: absolute;
    left: 36px;
    bottom: 30px;
    color: var(--white);
    font-size: 13px;
  }

  /* Back */
  .card--back {
    background: linear-gradient(160deg, var(--white) 0%, var(--paper) 60%, var(--paper-shade) 100%);
  }
  .back-brand {
    position: absolute;
    left: 36px;
    top: 58px;
    display: flex;
    align-items: center;
    gap: 14px;
  }
  .back-brand .brand-dot { width: 44px; height: 44px; background: var(--brand-blue); }
  .back-brand .brand-name { color: var(--brand-blue); }
  .holder {
    position: absolute;
    right: 30px;
    top: 112px;
    text-align: right;
  }
  .holder-name { color: var(--brand-blue); font-size: 22px; }
  .holder-role { color: var(--ink-grey); font-size: 13px; margin-top: 2px; }
  .holder-rule {
    position: absolute;
    right: 30px;
    top: 164px;
    width: 320px;
    height: 1px;
    background: var(--rule);
  }
  .contact {
    position: absolute;
    left: 36px;
    bottom: 34px;
    width: 468px;
    border-top: 1px solid var(--rule);
    padding-top: 10px;
    color: var(--ink-grey);
    font-size: 14px;
    line-height: 1.5;
  }
  .contact-row { display: flex; align-items: center; gap: 6px; white-space: nowrap; }
  .contact-row + .contact-row { margin-top: 1px; }
  .icon { width: 13px; height: 13px; fill: var(--brand-blue); flex: none; }
  .contact-gap { width: 10px; }
</style>
</head>
<body>

  <section class="card card--front" aria-label="Business card front">
    <div class="front-artwork" role="img" aria-label="Large glowing blue abstract brand artwork"></div>
    <div class="front-brand">
      <span class="brand-dot"></span>
      <span class="brand-name">Red Anvil Workforce Staff</span>
    </div>
    <p class="front-web">www.redanvilworkforce.example.com.au</p>
  </section>

  <section class="card card--back" aria-label="Business card back">
    <div class="back-brand">
      <span class="brand-dot"></span>
      <span class="brand-name">Red Anvil Workforce Staff</span>
    </div>

    <div class="holder">
      <p class="holder-name">Neil Dawson</p>
      <p class="holder-role">Managing Director</p>
    </div>
    <div class="holder-rule"></div>

    <div class="contact">
      <p class="contact-row">
        <svg class="icon" viewBox="0 0 24 24" aria-hidden="true"><path d="M12 1a8 8 0 0 0-8 8c0 6 8 14 8 14s8-8 8-14a8 8 0 0 0-8-8zm0 11a3 3 0 1 1 0-6 3 3 0 0 1 0 6z"/></svg>
        417 Tamber Road Marrowdale Northshire 6190
      </p>
      <p class="contact-row">
        <svg class="icon" viewBox="0 0 24 24" aria-hidden="true"><path d="M2 9c0-3 4-5 10-5s10 2 10 5v2h-5V9c-2-1-8-1-10 0v2H2zm4 3h12l2 9H4z"/></svg>
        08 9471 3826
        <span class="contact-gap"></span>
        <svg class="icon" viewBox="0 0 24 24" aria-hidden="true"><path d="M7 1h10a2 2 0 0 1 2 2v18a2 2 0 0 1-2 2H7a2 2 0 0 1-2-2V3a2 2 0 0 1 2-2zm0 3v13h10V4zm5 15a1.3 1.3 0 1 0 0 2.6A1.3 1.3 0 0 0 12 19z"/></svg>
        0477 863 150
      </p>
      <p class="contact-row">
        <svg class="icon" viewBox="0 0 24 24" aria-hidden="true"><path d="M2 5h20v14H2zm2 2v1l8 5 8-5V7l-8 5z"/></svg>
        neild@redanvilworkforce.example.com.au
      </p>
    </div>
  </section>

</body>
</html>
```